3rd Package added to brochure design

Please see attached brochure. Appreciate your continued support in this endeavor.

We modified the interior packages to provide a bit more of a separate feel to the packages.

The source files to the new brochure with modified packages are labeled under the mosaic bench link below.

When we physically printed the brochure I noted some additional edits about the brochure please see the youtube https://vidloop.example/w/Kp3vQm8LzRa .

This video explains a majority of the edits requested. The attached image also has the edits physically on the brochure.

https://vidloop.example/w/Kp3vQm8LzRa

Ive also typed the edits needed in here.

FRONT OF BROCHURE
Top of the brochure

These are the previous 3 FRONT brochures and/or designs that we like.
We have to incorporate more of Our Vantor Color blue on the front. Image 23 24 and 25

Lets see the brochure with this image on the front instead of the family as well.

The source file for one of the above images is below is in the below we transfer file if its helpful https://filedrop.example/t-QmRp8ZxLva

Also, in the brochure we want to add a 3rd package and remove the checkmark comparison inside the brochure

The 3rd package will be called platinum. and have the following benefits added.

Please notice cobalt finch added to the plus package

Target Market(s)

Real Estate Agents

Industry/Entity Type

Home Inspection

Requirements
Must have
• Branded colors

```html
<!DOCTYPE html>
<html lang="en">
<head>
<meta charset="utf-8">
<title>Vantor Group Inspection Brochure</title>
<link href="https://fonts.googleapis.com/css2?family=Montserrat:wght@500;700;800&family=Open+Sans:wght@400;600&display=swap" rel="stylesheet">
<style>
:root{
  --bg:#6d6d6d;
  --navy:#0c2b5c;
  --blue:#1c5aa6;
  --sky:#2f86d6;
  --yellow:#f4b400;
  --green:#79b443;
  --platinum:#8e9aab;
  --ink:#2a2f3a;
  --muted:#6b7482;
  --white:#ffffff;
}
*{box-sizing:border-box;margin:0;padding:0}
html,body{width:849px;height:1200px;overflow:hidden}
body{background:var(--bg);font-family:"Open Sans",Arial,sans-serif;color:var(--ink);position:relative}
.sheet{position:absolute;left:56px;width:737px;height:552px;background:var(--white);display:flex;box-shadow:0 4px 14px rgba(0,0,0,.35);overflow:hidden}
.sheet.outside{top:18px}
.sheet.inside{top:612px}
.panel{width:245.6px;height:100%;position:relative;overflow:hidden;flex:none}
h2,h3,h4,.brand,.phone-big{font-family:"Montserrat",Arial,sans-serif}
.band{background:var(--navy);color:var(--white);font-family:"Montserrat",Arial,sans-serif;font-weight:800;font-size:12px;letter-spacing:.5px;padding:9px 14px}
.tiny{font-size:6.2px;line-height:1.45;color:var(--muted)}
.brand{display:flex;align-items:center;gap:6px;font-weight:800;font-size:15px;color:var(--white)}
.brand .dot{width:18px;height:18px;border-radius:50%;background:var(--white)}
.brand.dark{color:var(--navy)}
.brand.dark .dot{background:var(--navy)}
.badge{width:26px;height:26px;border-radius:50%;background:#c9d3df;border:2px solid var(--blue);display:block}

/* outside left */
.services{padding:8px 12px}
.service{margin-bottom:7px}
.service h4{background:var(--blue);color:var(--white);font-size:6.5px;font-weight:700;padding:2px 6px;display:inline-block;margin-bottom:2px}
.badges{display:flex;gap:9px;justify-content:center;padding:4px 0}
.services-foot{position:absolute;bottom:0;left:0;right:0;background:var(--navy);color:var(--white);padding:7px 12px;text-align:center}
.services-foot h3{font-size:11px;font-weight:800;margin-bottom:3px}
.services-foot .tiny{color:#cfe0f5}

/* outside middle */
.mid-top{background:var(--navy);height:62px;display:flex;align-items:center;justify-content:center}
.mid-body{background:var(--blue);padding:10px 14px;height:250px;color:var(--white)}
.mid-body h3{font-size:9px;font-weight:700;margin:6px 0 3px;text-align:center}
.mid-body .tiny{color:#dbe8f8}
.mid-body .box{background:var(--navy);padding:6px 8px;margin-top:6px}
.cta{background:var(--white);color:var(--blue);font-family:"Montserrat",Arial,sans-serif;font-weight:800;font-size:8px;text-align:center;padding:5px;margin-top:8px}
.contact{padding:12px 16px}
.pill{background:var(--navy);color:var(--white);font-family:"Montserrat",Arial,sans-serif;font-weight:700;font-size:8px;border-radius:10px;padding:4px 12px;display:inline-block;margin-bottom:8px}
.contact-row{display:flex;align-items:center;gap:7px;font-size:7.5px;margin-bottom:7px}
.contact-row svg{flex:none}
.mid-foot{position:absolute;bottom:14px;left:0;right:0;display:flex;justify-content:center;gap:10px}
.mid-foot .badge{width:34px;height:34px}

/* cover */
.cover-head{height:52px;display:flex;align-items:center;justify-content:center}
.cover-photo{height:210px;background:linear-gradient(160deg,#a9c4de 0%,#dfe7ee 45%,#8a9a7c 75%,#3f6f8f 100%)}
.cover-band{background:var(--navy);color:var(--white);height:290px;padding:16px 18px;text-align:center}
.cover-band h2{font-size:17px;font-weight:800;line-height:1.15;margin-bottom:6px}
.cover-band .tiny{color:#cfe0f5}
.cover-badges{display:flex;justify-content:center;gap:14px;margin:22px 0}
.cover-badges .badge{width:44px;height:44px;background:#dfe7f1}
.phone-big{font-size:22px;font-weight:800;letter-spacing:.5px;margin-top:8px}
.url{font-size:7.5px;color:#cfe0f5;margin-top:3px}

/* inside */
.inside-left{width:491.2px;height:100%;display:flex;flex-direction:column;flex:none}
.options{display:flex;flex:1}
.option{width:50%;padding:8px 10px}
.option+.option{border-left:1px solid #dde3ea}
.tab{border-radius:4px 4px 0 0;text-align:center;padding:5px 4px 6px}
.tab small{display:inline-block;font-family:"Montserrat",Arial,sans-serif;font-weight:800;font-size:7px;background:var(--white);border-radius:8px;padding:1px 8px;margin-bottom:2px}
.tab h3{font-size:9.5px;font-weight:800;color:var(--white);line-height:1.15}
.tab.standard{background:var(--yellow)}
.tab.standard small{color:#b98600}
.tab.plus{background:var(--green)}
.tab.plus small{color:#4f8a22}
.tab.platinum{background:var(--platinum)}
.tab.platinum small{color:#5c6878}
.item{display:flex;gap:6px;margin-top:7px}
.icon{width:16px;height:16px;border-radius:50%;flex:none;background:var(--blue)}
.item h4{font-size:6.3px;font-weight:700;color:var(--navy)}
.intro{margin-top:6px;text-align:center}
.benefits{background:var(--navy);color:var(--white);font-family:"Montserrat",Arial,sans-serif;font-weight:800;font-size:8px;padding:4px 8px;margin-top:8px}

.inside-right{width:245.8px;height:100%;background:var(--blue);color:var(--white);padding:12px;position:relative;flex:none}
.pkg-title{display:flex;align-items:center;gap:6px;margin-bottom:8px}
.pkg-title b{font-family:"Montserrat",Arial,sans-serif;font-size:30px;font-weight:800;line-height:1}
.pkg-title span{font-family:"Montserrat",Arial,sans-serif;font-size:11px;font-weight:800;line-height:1.1}
.plat-card{background:var(--white);padding:0 0 8px;color:var(--ink)}
.plat-card .items{padding:0 10px}
.pay{text-align:center;margin-top:12px}
.pay h3{font-size:10px;font-weight:800;line-height:1.2}
.pay .chip{display:inline-block;background:var(--yellow);color:var(--navy);font-family:"Montserrat",Arial,sans-serif;font-weight:800;font-size:8px;padding:3px 12px;margin-top:4px}
.right-foot{position:absolute;bottom:12px;left:0;right:0;text-align:center}
.right-foot .brand{justify-content:center;font-size:13px}
.right-foot .phone-big{font-size:18px;margin-top:4px}
</style>
</head>
<body>

<section class="sheet outside">
  <div class="panel">
    <div class="band">ADDITIONAL SERVICES</div>
    <div class="services">
      <div class="service"><h4>RADON GAS TESTING</h4><p class="tiny">A short in-home test measures radon levels over two days and reports clear results with next steps.</p></div>
      <div class="service"><h4>MOLD ASSESSMENT</h4><p class="tiny">Air and surface samples are taken in key areas and reviewed by an outside lab for accuracy.</p></div>
      <div class="service"><h4>SEWER SCOPE INSPECTION</h4><p class="tiny">A camera travels the main line to spot roots, cracks or sagging pipes before they cause trouble.</p></div>
      <div class="service"><h4>POOL &amp; SPA INSPECTION</h4><p class="tiny">Pumps, heaters, filters and surfaces are checked for safe and reliable operation.</p></div>
      <div class="service"><h4>THERMAL IMAGING</h4><p class="tiny">Infrared scans reveal hidden moisture, missing insulation and hot electrical points.</p></div>
      <div class="service"><h4>WOOD DESTROYING ORGANISMS</h4><p class="tiny">Our licensed team looks for termites and related damage.</p></div>
      <div class="service"><h4>PRE-LISTING INSPECTION</h4><p class="tiny">Help sellers price with confidence and avoid late surprises.</p></div>
    </div>
    <div class="badges"><span class="badge"></span><span class="badge"></span><span class="badge"></span><span class="badge"></span></div>
    <div class="services-foot">
      <h3>SERVICES</h3>
      <p class="tiny">Residential, commercial and new construction inspections across the region, seven days a week.</p>
    </div>
  </div>

  <div class="panel">
    <div class="mid-top"><div class="brand"><span class="dot"></span>VANTORGROUP</div></div>
    <div class="mid-body">
      <h3>Here's Something</h3>
      <p class="tiny">We deliver detailed, easy-to-read reports within twenty-four hours, complete with photos and clear notes for buyers and agents.</p>
      <div class="box">
        <h3>Our Promise</h3>
        <p class="tiny">Every inspector is certified, insured and trained to look closer so your clients can close with confidence.</p>
      </div>
      <div class="box">
        <p class="tiny">Flexible scheduling, fast reports and a friendly team ready to answer questions long after the visit.</p>
      </div>
      <div class="cta">BOOK YOUR INSPECTION TODAY</div>
    </div>
    <div class="contact">
      <div style="text-align:center"><span class="pill">CONTACT US</span></div>
      <div class="contact-row"><svg width="12" height="12" viewBox="0 0 24 24"><circle cx="12" cy="12" r="12" fill="#1c5aa6"/><path d="M8 6l2 0 1 3-1.5 1a8 8 0 0 0 4 4l1-1.5 3 1 0 2a1 1 0 0 1-1 1A10 10 0 0 1 7 7a1 1 0 0 1 1-1z" fill="#fff"/></svg>(800) 555-0142</div>
      <div class="contact-row"><svg width="12" height="12" viewBox="0 0 24 24"><circle cx="12" cy="12" r="12" fill="#1c5aa6"/><rect x="6" y="8" width="12" height="8" fill="none" stroke="#fff" stroke-width="1.5"/><path d="M6 8l6 5 6-5" fill="none" stroke="#fff" stroke-width="1.5"/></svg>hello@vantorgroup.example</div>
      <div class="contact-row"><svg width="12" height="12" viewBox="0 0 24 24"><circle cx="12" cy="12" r="12" fill="#1c5aa6"/><circle cx="12" cy="12" r="6" fill="none" stroke="#fff" stroke-width="1.5"/><path d="M6 12h12M12 6v12" stroke="#fff" stroke-width="1.2"/></svg>www.vantorgroup.example</div>
    </div>
    <div class="mid-foot"><span class="badge"></span><span class="badge"></span><span class="badge"></span></div>
  </div>

  <div class="panel">
    <div class="cover-head"><div class="brand dark"><span class="dot"></span>VANTORGROUP</div></div>
    <div class="cover-photo" role="img" aria-label="Photo of a modern two-storey home with a pool at dusk"></div>
    <div class="cover-band">
      <h2>HOME INSPECTIONS<br>DONE RIGHT</h2>
      <p class="tiny">Trusted by agents, buyers and sellers for thorough, on-time inspections.</p>
      <div class="cover-badges"><span class="badge"></span><span class="badge"></span></div>
      <div class="phone-big">800 - 555 - 0142</div>
      <div class="url">www.vantorgroup.example</div>
    </div>
  </div>
</section>

<section class="sheet inside">
  <div class="inside-left">
    <div class="band" style="font-size:12.5px;padding:11px 16px">CHOOSE BETWEEN OUR INSPECTION PACKAGES</div>
    <div class="options">
      <div class="option">
        <div class="tab standard"><small>OPTION 1</small><h3>STANDARD<br>HOME INSPECTION</h3></div>
        <div class="item"><span class="icon"></span><div><h4>STRUCTURE INSPECTION</h4><p class="tiny">Foundation, framing and roof are checked for wear and defects.</p></div></div>
        <div class="item"><span class="icon"></span><div><h4>COMPREHENSIVE SYSTEMS CHECK</h4><p class="tiny">Electrical, plumbing and heating reviewed room by room.</p></div></div>
        <div class="item"><span class="icon"></span><div><h4>HD PHOTO REPORT</h4><p class="tiny">Clear images and notes sent within one business day.</p></div></div>
        <div class="item"><span class="icon"></span><div><h4>RESULTS YOU CAN TRUST</h4><p class="tiny">Certified inspectors follow a strict checklist.</p></div></div>
        <div class="benefits">BENEFITS INCLUDE</div>
        <div class="item"><span class="icon"></span><div><h4>MAINTENANCE REMINDERS</h4><p class="tiny">Seasonal tips after closing.</p></div></div>
        <div class="item"><span class="icon"></span><div><h4>DISCOUNTED FOLLOW-UPS</h4><p class="tiny">Savings on re-inspections.</p></div></div>
        <div class="item"><span class="icon"></span><div><h4>APPLIANCE RECALL CHECK</h4><p class="tiny">We search for known recalls.</p></div></div>
      </div>
      <div class="option">
        <div class="tab plus"><small>OPTION 2</small><h3>VANTOR PLUS<br>HOME INSPECTION</h3></div>
        <p class="tiny intro">Includes everything in the standard package, plus:</p>
        <div class="item"><span class="icon"></span><div><h4>THERMAL IMAGING SCAN</h4><p class="tiny">Infrared camera finds hidden leaks and heat loss.</p></div></div>
        <div class="item"><span class="icon"></span><div><h4>SEWER LINE CAMERA</h4><p class="tiny">Main line scoped from house to street.</p></div></div>
        <div class="item"><span class="icon"></span><div><h4>COBALT FINCH AUDIT</h4><p class="tiny">Energy use review with simple savings advice.</p></div></div>
        <div class="item"><span class="icon"></span><div><h4>ROOF DRONE VIEW</h4><p class="tiny">Aerial images of hard-to-reach roof areas.</p></div></div>
        <div class="item"><span class="icon"></span><div><h4>90-DAY WARRANTY</h4><p class="tiny">Coverage for major systems after closing.</p></div></div>
        <div class="item"><span class="icon"></span><div><h4>UPGRADE &amp; REPAIR ESTIMATE</h4><p class="tiny">Budget ranges for noted repairs.</p></div></div>
        <div class="item"><span class="icon"></span><div><h4>PRIORITY SCHEDULING</h4><p class="tiny">Next-day booking when available.</p></div></div>
      </div>
    </div>
  </div>

  <div class="inside-right">
    <div class="pkg-title"><b>3</b><span>SERVICE<br>PACKAGES</span></div>
    <div class="plat-card">
      <div class="tab platinum"><small>OPTION 3</small><h3>PLATINUM<br>HOME INSPECTION</h3></div>
      <div class="items">
        <p class="tiny intro">Includes everything in the plus package, plus:</p>
        <div class="item"><span class="icon"></span><div><h4>MOLD &amp; AIR QUALITY TEST</h4><p class="tiny">Lab-reviewed samples from key rooms.</p></div></div>
        <div class="item"><span class="icon"></span><div><h4>RADON MONITORING</h4><p class="tiny">Two-day continuous radon reading.</p></div></div>
        <div class="item"><span class="icon"></span><div><h4>POOL &amp; SPA REVIEW</h4><p class="tiny">Pumps, heaters and surfaces checked.</p></div></div>
        <div class="item"><span class="icon"></span><div><h4>1-YEAR WARRANTY</h4><p class="tiny">Extended coverage on major systems.</p></div></div>
        <div class="item"><span class="icon"></span><div><h4>WALK-THROUGH CONSULT</h4><p class="tiny">Live review of findings with your inspector.</p></div></div>
      </div>
    </div>
    <div class="pay">
      <h3>PAYMENT AT<br>CLOSE OF ESCROW</h3>
      <span class="chip">AVAILABLE</span>
    </div>
    <div class="right-foot">
      <div class="brand"><span class="dot"></span>VANTORGROUP</div>
      <div class="phone-big">800 - 555 - 0142</div>
      <div class="url">www.vantorgroup.example</div>
    </div>
  </div>
</section>

</body>
</html>
```